Stationery Design Project

QV7 Staffing requires letterhead and business card designs for a company based in London. Just like the name, we're a management resourcing company, providing resources to third party companies. You can see www.qv7staffing-example.com for ideas on existing colour schemes and design concepts that have been implimented and agreed to. Ultimately the design should broadcast professionalism, safety and the concept of growth.

Target Market(s)

Financial institutes; friendly societies (All UK based)

Industry/Entity Type

Safety

Requirements
Must have
• Files produced should be print ready; and the text in them editable (eg address, name etc)

```html
<!DOCTYPE html>
<html lang="en">
<head>
<meta charset="utf-8">
<title>QV7 Staffing Stationery</title>
<link href="https://fonts.googleapis.com/css2?family=Questrial&display=swap" rel="stylesheet">
<style>
:root{
  --slate:#5f6363;
  --slate-dark:#383c3b;
  --slate-mid:#5a605f;
  --teal:#1b8b8c;
  --sky:#7cc0e1;
  --paper:#ffffff;
  --card-light:#f5f5f5;
  --card-shade:#e4e4e4;
  --ink:#3a3a3a;
  --muted:#8a8a8a;
}
*{box-sizing:border-box;margin:0;padding:0}
html,body{width:1200px;height:1133px;overflow:hidden;background:#fff}
body{position:relative;font-family:"Questrial",sans-serif}
.sheet{position:absolute;overflow:hidden}
.bar{position:absolute}
.bar--teal{background:var(--teal)}
.bar--sky{background:var(--sky)}
.brand-name{position:absolute;white-space:nowrap;color:var(--sky);letter-spacing:1px;line-height:1}

/* Folder cover */
.cover{left:14px;top:14px;width:578px;height:743px;
  background:radial-gradient(ellipse at 55% 40%,var(--slate-mid) 0%,var(--slate-dark) 80%)}
.cover__header{position:absolute;left:0;top:0;width:100%;height:113px;background:var(--slate)}
.cover__footer{position:absolute;left:0;top:636px;width:100%;height:107px;background:var(--slate)}
.cover__namebox{position:absolute;left:0;top:643px;width:267px;height:66px;background:var(--teal)}
.cover__endbox{position:absolute;left:539px;top:643px;width:39px;height:66px;background:var(--sky)}
.cover__person{position:absolute;left:26px;top:652px;font-size:21px;color:#e9f4f4}
.cover__company{position:absolute;right:318px;top:682px;font-size:13px;color:#1f3737;text-align:right}
.contact-list{position:absolute;list-style:none}
.contact-list li{display:flex;align-items:center;gap:6px;white-space:nowrap}
.contact-list svg{flex:none}
.cover .contact-list{left:305px;top:648px;color:var(--sky);font-size:15px}
.cover .contact-list li{height:20px}

/* Letterhead */
.letter{left:607px;top:14px;width:578px;height:743px;background:var(--paper)}
.letter__header{position:absolute;left:0;top:0;width:100%;height:98px;background:var(--slate)}
.letter__footer{position:absolute;left:0;top:682px;width:100%;height:61px;background:var(--slate);
  color:var(--sky);font-size:17px;letter-spacing:2px;text-align:center;line-height:61px}
.letter__recipient{position:absolute;left:376px;top:150px;font-size:10px;line-height:18px;color:var(--muted)}
.letter__body{position:absolute;left:58px;top:244px;width:470px;font-size:10.5px;line-height:14px;color:var(--muted)}
.letter__body p{margin-bottom:14px}

/* Card back */
.card-back{left:14px;top:776px;width:578px;height:343px;
  background:radial-gradient(ellipse at 50% 35%,#676c6b 0%,var(--slate-dark) 75%)}

/* Card front */
.card-front{left:607px;top:776px;width:578px;height:343px;
  background:linear-gradient(180deg,var(--card-light) 0%,var(--card-shade) 90%)}
.card-front__strip{position:absolute;left:0;top:315px;width:100%;height:28px;background:var(--slate)}
.card-front__person{position:absolute;left:39px;top:172px;font-size:20px;color:var(--teal)}
.card-front__company{position:absolute;left:60px;top:196px;font-size:13px;color:var(--ink)}
.card-front .contact-list{top:238px;color:var(--ink);font-size:13px}
.card-front .contact-list li{height:17.5px}
.card-front .contact-list--main{left:39px}
.card-front .contact-list--web{left:270px}
</style>
</head>
<body>

<section class="sheet cover" aria-label="Folder cover">
  <div class="cover__header">
    <span class="brand-name" style="left:50px;top:52px;font-size:30px">QV7 STAFFING</span>
    <div class="bar bar--teal" style="left:379px;top:38px;width:199px;height:17px"></div>
    <div class="bar bar--sky" style="left:300px;top:65px;width:278px;height:36px"></div>
  </div>
  <div class="cover__footer"></div>
  <div class="cover__namebox"></div>
  <div class="cover__endbox"></div>
  <p class="cover__person">First, Last Name</p>
  <p class="cover__company">QV7 Staffing</p>
  <ul class="contact-list">
    <li><svg width="14" height="14" viewBox="0 0 14 14"><circle cx="7" cy="7" r="7" fill="#7cc0e1"/><path d="M7 3a2.5 2.5 0 0 0-2.5 2.5C4.5 8 7 11 7 11s2.5-3 2.5-5.5A2.5 2.5 0 0 0 7 3z" fill="#5f6363"/></svg>Address, Country Zipcode</li>
    <li><svg width="14" height="14" viewBox="0 0 14 14"><circle cx="7" cy="7" r="6.3" fill="none" stroke="#7cc0e1" stroke-width="1.4"/><path d="M5 4l1.2 1.6-.7.9c.5 1 1.2 1.7 2 2l.9-.7L10 9l-.8 1.2C7 10 4.2 7.2 4 4.8z" fill="#7cc0e1"/></svg>123.456.7890</li>
    <li><svg width="14" height="14" viewBox="0 0 14 14"><circle cx="7" cy="7" r="7" fill="#7cc0e1"/><rect x="3.5" y="4.5" width="7" height="5" fill="#5f6363"/><path d="M3.5 4.5L7 7.5l3.5-3" stroke="#7cc0e1" fill="none"/></svg>hello@qv7staffing-example.com</li>
  </ul>
</section>

<section class="sheet letter" aria-label="Letterhead">
  <div class="letter__header">
    <span class="brand-name" style="left:22px;top:50px;font-size:18px">QV7 STAFFING</span>
    <div class="bar bar--teal" style="left:166px;top:45px;width:405px;height:13px"></div>
    <div class="bar bar--sky" style="left:159px;top:65px;width:412px;height:26px"></div>
  </div>
  <div class="letter__recipient">
    <p>Ms Jane Carter</p>
    <p>Finance Director</p>
    <p>London EC2A 4NE</p>
  </div>
  <div class="letter__body">
    <p>Dear Ms Carter,</p>
    <p>Thank you for meeting with our team last week. We are pleased to confirm the resourcing plan we discussed for your finance department, with interim managers ready to start from the first of next month.</p>
    <p>Each placement is screened and fully vetted before arrival.</p>
    <p>Our consultants will stay in close contact throughout the assignment, reviewing progress with you every fortnight and adjusting support as your needs grow.</p>
    <p>Please find the proposed schedule and terms enclosed. If anything needs changing, simply reply to this letter or call us directly and we will update the plan.</p>
    <p>We look forward to working with you. Kind regards, Daniel Hughes</p>
  </div>
  <div class="letter__footer">www.qv7staffing-example.com</div>
</section>

<section class="sheet card-back" aria-label="Business card back">
  <span class="brand-name" style="left:60px;top:116px;font-size:40px">QV7 STAFFING</span>
  <div class="bar bar--teal" style="left:380px;top:127px;width:198px;height:29px"></div>
  <div class="bar bar--sky" style="left:315px;top:168px;width:263px;height:56px"></div>
</section>

<section class="sheet card-front" aria-label="Business card front">
  <span class="brand-name" style="left:22px;top:36px;font-size:32px;color:var(--teal)">QV7 STAFFING</span>
  <div class="bar bar--teal" style="left:405px;top:40px;width:173px;height:24px"></div>
  <div class="bar bar--sky" style="left:228px;top:77px;width:350px;height:39px"></div>
  <p class="card-front__person">First, Last Name</p>
  <p class="card-front__company">QV7 Staffing</p>
  <ul class="contact-list contact-list--main">
    <li><svg width="12" height="12" viewBox="0 0 14 14"><circle cx="7" cy="7" r="7" fill="#1b8b8c"/><path d="M7 3a2.5 2.5 0 0 0-2.5 2.5C4.5 8 7 11 7 11s2.5-3 2.5-5.5A2.5 2.5 0 0 0 7 3z" fill="#fff"/></svg>Address, Country Zipcode</li>
    <li><svg width="12" height="12" viewBox="0 0 14 14"><circle cx="7" cy="7" r="6.3" fill="none" stroke="#1b8b8c" stroke-width="1.4"/><path d="M5 4l1.2 1.6-.7.9c.5 1 1.2 1.7 2 2l.9-.7L10 9l-.8 1.2C7 10 4.2 7.2 4 4.8z" fill="#1b8b8c"/></svg>123.456.7890</li>
    <li><svg width="12" height="12" viewBox="0 0 14 14"><circle cx="7" cy="7" r="7" fill="#1b8b8c"/><rect x="3.5" y="4.5" width="7" height="5" fill="#fff"/><path d="M3.5 4.5L7 7.5l3.5-3" stroke="#1b8b8c" fill="none"/></svg>hello@qv7staffing-example.com</li>
  </ul>
  <ul class="contact-list contact-list--web">
    <li><svg width="12" height="12" viewBox="0 0 14 14"><circle cx="7" cy="7" r="7" fill="#1b8b8c"/></svg>social.example/QV7</li>
    <li><svg width="12" height="12" viewBox="0 0 14 14"><circle cx="7" cy="7" r="7" fill="#1b8b8c"/></svg>www.friendbook-example.com/QV7</li>
    <li><svg width="12" height="12" viewBox="0 0 14 14"><circle cx="7" cy="7" r="6.3" fill="none" stroke="#1b8b8c" stroke-width="1.4"/><path d="M1 7h12M7 1v12" stroke="#1b8b8c"/></svg>www.qv7staffing-example.com</li>
  </ul>
  <div class="card-front__strip"></div>
</section>

</body>
</html>
```